Bref créative
VORLAQ
Stationary Design
Simple
Tamer H. Bin Ruqail
Executive Director - Partner
P. O. Box 81726
Jeddah, 23847
Saudi Arabia
thruqail@vorlaq-mail.net
www.vorlaq-web.net
CR No. 7192836450
The CR should appear only on the stationary, and not on the business cards.
The stationary should be bilingual English and Arabic.
The Arabic text for the address information is as follows.
P. O. Box = ص. ب
Jeddah = جدة
Saudi Arabia = المملكة العربية السعودية
CR = س. ت
Numbers are the same in both languages.
I ask the designer to use best judgment in selecting the font to be used on the card.
The back of the business card, will mirror the front of it as it will be used for the Arabic information.
It will have the same information as listed above.

```html
<!DOCTYPE html>
<html lang="en">
<head>
<meta charset="utf-8">
<title>VORLAQ Presentation Folder</title>
<link rel="stylesheet" href="https://fonts.googleapis.com/css2?family=Cinzel:wght@400;600&family=Roboto:wght@400&family=Noto+Naskh+Arabic:wght@400&display=swap">
<style>
  :root {
    --backdrop: #5a5a5a;
    --black: #0b0b0b;
    --charcoal: #1c1c1c;
    --red: #c4262a;
    --red-dark: #7e1316;
    --white: #ffffff;
    --paper-shade: #e4e2de;
    --muted: #9a9a9a;
  }
  html, body {
    margin: 0;
    padding: 0;
    width: 1200px;
    height: 559px;
    overflow: hidden;
    background: var(--backdrop);
  }
  .stage {
    position: relative;
    width: 1200px;
    height: 559px;
  }
  .folder-front {
    position: absolute;
    left: 48px;
    top: 36px;
    width: 512px;
    height: 497px;
    box-shadow: 0 10px 24px rgba(0,0,0,.45);
  }
  .folder-inside {
    position: absolute;
    left: 631px;
    top: 72px;
    width: 533px;
    height: 444px;
    box-shadow: 0 10px 24px rgba(0,0,0,.4);
  }
  svg { display: block; }
  .tagline {
    font-family: "Cinzel", serif;
    font-size: 17px;
    fill: var(--white);
    letter-spacing: .5px;
  }
  .brand-name {
    font-family: "Cinzel", serif;
    font-weight: 600;
    font-size: 15px;
    fill: var(--white);
    letter-spacing: 3px;
  }
  .address-line {
    font-family: "Roboto", sans-serif;
    font-size: 6.5px;
    fill: var(--muted);
  }
  .address-line-ar {
    font-family: "Noto Naskh Arabic", serif;
    font-size: 7px;
    fill: var(--muted);
    direction: rtl;
    unicode-bidi: embed;
  }
</style>
</head>
<body>
<main class="stage">

  <section class="folder-front" aria-label="Folder front cover">
    <svg width="512" height="497" viewBox="0 0 512 497">
      <defs>
        <linearGradient id="red-panel-fill" x1="0" y1="0" x2="1" y2="1">
          <stop offset="0" stop-color="var(--red)"/>
          <stop offset="1" stop-color="var(--red-dark)"/>
        </linearGradient>
        <linearGradient id="base-band-fill" x1="0" y1="0" x2="0" y2="1">
          <stop offset="0" stop-color="#2a2a2a"/>
          <stop offset="1" stop-color="var(--black)"/>
        </linearGradient>
      </defs>
      <rect class="cover-ground" width="512" height="497" fill="var(--black)"/>
      <path class="red-panel" d="M150 0 H512 V300 Q330 322 150 350 Z" fill="url(#red-panel-fill)"/>
      <path class="base-band" d="M0 430 Q250 338 512 306 V497 H0 Z" fill="url(#base-band-fill)"/>
      <path class="sweep-line" d="M0 430 Q250 338 512 306" fill="none" stroke="var(--white)" stroke-width="1.6" opacity=".9"/>
      <text class="tagline" x="335" y="378" text-anchor="middle">Your Tagline Goes Here</text>
      <rect class="brand-square" x="350" y="398" width="20" height="20" fill="var(--red)"/>
      <text class="brand-name" x="360" y="440" text-anchor="middle">VORLAQ</text>

      <rect class="brand-square" x="36" y="414" width="18" height="18" fill="var(--red)"/>
      <g class="address-block-en">
        <text class="address-line" x="20" y="452">P. O. Box 81726, Jeddah, 23847</text>
        <text class="address-line" x="20" y="462">Saudi Arabia, CR No. 7192836450</text>
        <text class="address-line" x="20" y="472">www.vorlaq-web.net</text>
      </g>
      <g class="address-block-ar">
        <text class="address-line-ar" x="250" y="452" text-anchor="start">ص. ب 81726، جدة 23847</text>
        <text class="address-line-ar" x="250" y="462" text-anchor="start">المملكة العربية السعودية، س. ت 7192836450</text>
      </g>
    </svg>
  </section>

  <section class="folder-inside" aria-label="Folder inside with pockets">
    <svg width="533" height="444" viewBox="0 0 533 444">
      <defs>
        <linearGradient id="left-panel-shade" x1="0" y1="0" x2="1" y2="0">
          <stop offset="0" stop-color="var(--white)"/>
          <stop offset=".85" stop-color="var(--white)"/>
          <stop offset="1" stop-color="var(--paper-shade)"/>
        </linearGradient>
        <linearGradient id="right-panel-shade" x1="0" y1="0" x2="1" y2="0">
          <stop offset="0" stop-color="var(--paper-shade)"/>
          <stop offset=".15" stop-color="var(--white)"/>
          <stop offset="1" stop-color="var(--white)"/>
        </linearGradient>
      </defs>
      <rect class="inside-panel-left" x="0" y="0" width="266" height="444" fill="url(#left-panel-shade)"/>
      <rect class="inside-panel-right" x="266" y="0" width="267" height="444" fill="url(#right-panel-shade)"/>
      <path class="pocket-left" d="M0 338 L252 350 L263 444 H0 Z" fill="var(--black)"/>
      <path class="pocket-right" d="M533 338 L281 350 L270 444 H533 Z" fill="var(--black)"/>
      <path class="pocket-notch" d="M262 444 L266 398 L271 444 Z" fill="var(--charcoal)"/>
    </svg>
  </section>

</main>
</body>
</html>
```